Logo and label design for our product coffee scrub

We need a logo design and a packaging label design for our new brand called "Rocco Velvetine". Best design wins 500$

It's a cosmetic brand with initial product "coffee scrub", which is a body peeling made of coffee, himalayan salt and additives. Brand will target young to middle aged women, who we will address with a very sexy and slightly provocative appeal (pictures of women wearing nothing but our coffee scrub - sample attached). Purpose of the coffee scrub is to target cellulite, stretch marks, psoriasis, varicose veins, eczema and acne.

Packaging that we will use will be a brown stand up pouch (attached) with a dimensions width 13cm, height 22cm and with a front and back sticker (dimensions width 7cm, height 14cm, round corners) or sticker that overlaps from front to back.

Looking forward on receiving your ideas!

Target Market(s)

Brand will targeting young to middle aged european women, who we will address with a very sexy and slightly provocative appeal (pictures of women wearing nothing but our coffee scrub - sample attached)

Industry/Entity Type

Product

Requirements
Must have
• Just an idea for the logo writing to use a handwriting font "Rocco Velvetine".

For the front side of packaging label you could use a picture of a women's body wearing a coffee scrub. Label should be very sexy but not vulgar.
Nice to have
• The back side of the label should have a cheesy pick up line and declaration text (just a sample):

hi babe! so you wanna get dirty! just show me the way to your bath. but first let me give you a proper introduction of myself. my name is rocco and i'm a coffee scrub wearing nothing but 250g of finest arabic coffee and sweet orange flavour & lots of other good stuff.

by the way I will help you with cellulite, stretch marks, psoriasis, varicose veins, eczema and acne. i’ll smooth your lumps and bumps with brown sugar & sea salt, moisturise and tone your skin with cold pressed sweet almond oil, and use vitamins & minerals to work wonders from the outside in. then i’ll make us both smell good with a little orange essence.

ingredients:
Coffea Robusta Seed Powder (Coffee), Prunus Amygdalus Dulcis (Sweet Almond) Oil, Water (Aqua), Sodium Chloride (Salt), Sucrose (Brown Sugar). All ingredients organic.

net weight: 200 g

best before date:

barcode

```html
<!DOCTYPE html>
<html lang="en">
<head>
<meta charset="utf-8">
<title>Rocco Velvetine – Coffee Scrub Label</title>
<link href="https://fonts.googleapis.com/css2?family=Great+Vibes&family=Oswald:wght@500&family=Open+Sans:wght@400;700&display=swap" rel="stylesheet">
<style>
  :root {
    --page: #f2f0ee;
    --label-dark: #170c0e;
    --label-mid: #2a1418;
    --pink: #e0187f;
    --cream: #f3e6dc;
    --bean-dark: #2b160c;
    --bean-light: #6b3a1e;
    --skin-dark: #7a4a32;
    --skin-light: #c98f6c;
  }
  * { box-sizing: border-box; margin: 0; padding: 0; }
  html, body { width: 1200px; height: 900px; overflow: hidden; }
  body { background: var(--page); position: relative; }

  .label {
    position: absolute; left: 361px; top: 20px;
    width: 477px; height: 860px;
    border-radius: 22px; overflow: hidden;
    background: linear-gradient(180deg, var(--label-dark), var(--label-mid) 50%, var(--label-dark));
    font-family: "Open Sans", sans-serif;
  }

  .beans {
    position: absolute; left: 0; width: 100%;
    background: radial-gradient(ellipse at 30% 50%, var(--bean-light), var(--bean-dark) 70%);
  }
  .beans--top { top: 0; height: 73px; }
  .beans--bottom { top: 772px; height: 88px; }

  .rule { position: absolute; left: 0; width: 100%; height: 4px; background: var(--pink); }
  .rule--top { top: 79px; }
  .rule--bottom { top: 762px; }

  /* back panel, printed upside down */
  .back {
    position: absolute; left: 18px; top: 96px;
    width: 441px; height: 330px;
    transform: rotate(180deg);
    display: flex; flex-direction: column; justify-content: flex-end; gap: 14px;
    color: var(--cream); font-size: 10.5px; line-height: 1.45;
  }
  .back__copy { text-align: justify; }
  .ingredients {
    border: 1.5px solid var(--pink);
    padding: 8px 14px; text-align: center; font-size: 10px;
  }
  .ingredients__title { font-weight: 700; letter-spacing: 0.5px; }
  .back__meta {
    display: flex; justify-content: space-between;
    font-size: 10.5px; padding: 0 6px;
  }

  /* front panel */
  .front__photo {
    position: absolute; left: 0; top: 450px;
    width: 275px; height: 312px;
    background: radial-gradient(ellipse at 45% 40%, var(--skin-light), var(--skin-dark) 60%, var(--label-dark) 100%);
  }
  .brand {
    position: absolute; left: 288px; top: 488px; width: 176px;
    font-family: "Oswald", sans-serif; font-weight: 500;
    color: var(--pink); font-size: 34px; line-height: 1.15;
    letter-spacing: 1px; text-transform: uppercase; text-align: center;
  }
  .brand span { display: block; }

  .product {
    position: absolute; left: 286px; top: 628px;
    width: 180px; height: 46px;
    border: 2px solid var(--pink);
    display: flex; align-items: center; justify-content: center;
    font-family: "Oswald", sans-serif; font-weight: 500;
    color: var(--pink); font-size: 23px; letter-spacing: 1px;
  }
  .tagline {
    position: absolute; left: 286px; top: 686px; width: 182px;
    font-family: "Great Vibes", cursive;
    color: var(--cream); font-size: 20px; line-height: 1.05;
  }
</style>
</head>
<body>
  <article class="label">
    <div class="beans beans--top" role="img" aria-label="Band of roasted coffee beans"></div>
    <div class="rule rule--top"></div>

    <section class="back">
      <p class="back__copy">Hi babe! So you wanna get dirty! Just show me the way to your bath. But first let me give you a proper introduction of myself. My name is rocco and i'm a coffee scrub wearing nothing but 200g of finest arabic coffee and sweet orange flavour and lots of other good stuff.</p>
      <p class="back__copy">By the way I will help you with cellulite, stretch marks, psoriasis, varicose veins, eczema and acne. I'll smooth your lumps and bumps with brown sugar and sea salt, moisturise and tone your skin with cold pressed sweet almond oil, and use vitamins and minerals to work wonders from the outside in. Then i'll make us both smell good with a little orange essence.</p>
      <div class="ingredients">
        <p class="ingredients__title">INGREDIENTS:</p>
        <p>Coffea Robusta Seed Powder (Coffee), Prunus Amygdalus Dulcis (Sweet Almond) Oil, Water (Aqua), Sodium Chloride (Salt), Sucrose (Brown Sugar). All ingredients organic.</p>
      </div>
      <div class="back__meta">
        <span>Best before date:</span>
        <span>NET WT: 200 gms</span>
      </div>
    </section>

    <div class="front__photo" role="img" aria-label="Photograph of a woman covered in coffee scrub, looking over her shoulder"></div>
    <h1 class="brand"><span>Rocco</span><span>Velvetine</span></h1>
    <p class="product">COFFEE SCRUB</p>
    <p class="tagline">Body peeling made of coffee, himalayan salt and additives</p>

    <div class="rule rule--bottom"></div>
    <div class="beans beans--bottom" role="img" aria-label="Band of roasted coffee beans"></div>
  </article>
</body>
</html>
```